Business Card for Brevel Coatings

We need a simple, yet out standing business card for our painting company.

Target Market(s)

wealthy; high-end neighborhoods, and businesses

Industry/Entity Type

Painting

Contact Information for Business Card

Name:
Doran Vask

Email:
d.vask@brevel-coatings.com

Website:
Brevel-coatings.com

Phone Number:
(555) 416-9073

Font styles to use
Serif
Sans Serif

Requirements
Must have
• slogan "making change simple"
Should not have
• A title attached to the name on the card

```html
<!DOCTYPE html>
<html lang="en">
<head>
<meta charset="utf-8">
<title>Brevel Coatings – Business Card</title>
<link rel="stylesheet" href="https://fonts.googleapis.com/css2?family=Cinzel:wght@600&family=Arimo:wght@400;700&display=swap">
<style>
  :root {
    --olive-dark: #3f5c10;
    --olive: #4e7316;
    --lime: #a9c93a;
    --lime-light: #c4dc4e;
    --text-grey: #555a50;
    --paper: #ffffff;
    --backdrop: #e8e4dc;
  }
  * { box-sizing: border-box; margin: 0; padding: 0; }
  html, body { width: 1200px; height: 950px; overflow: hidden; }
  body {
    background: var(--backdrop);
    font-family: "Arimo", Arial, sans-serif;
    position: relative;
  }
  .card {
    position: absolute;
    width: 540px;
    height: 310px;
    overflow: hidden;
    border-radius: 4px;
    box-shadow: 0 6px 18px rgba(0,0,0,0.18);
  }
  .brand { display: flex; align-items: center; }
  .brand-square { flex: none; }
  .brand-name {
    font-family: "Cinzel", Georgia, serif;
    font-weight: 600;
    line-height: 1.05;
    white-space: nowrap;
  }
  .brand-name .line-main { display: block; letter-spacing: 1px; }
  .brand-name .line-sub { display: block; }

  /* Back side */
  .card-back {
    left: 80px; top: 130px;
    background: linear-gradient(135deg, var(--olive) 0%, var(--olive-dark) 100%);
    color: var(--paper);
  }
  .card-back .brand {
    position: absolute; left: 0; right: 0; top: 100px;
    justify-content: center; gap: 14px;
  }
  .card-back .brand-square { width: 44px; height: 44px; background: var(--lime-light); }
  .card-back .brand-name .line-main { font-size: 32px; }
  .card-back .brand-name .line-sub { font-size: 15px; letter-spacing: 8px; }
  .card-back .website {
    position: absolute; left: 0; right: 0; top: 200px;
    text-align: center; font-size: 13px; letter-spacing: 3px;
  }

  /* Front side */
  .card-front {
    left: 560px; top: 470px;
    background: var(--paper);
  }
  .card-front .brand {
    position: absolute; left: 36px; top: 48px;
    gap: 10px;
    color: var(--olive);
  }
  .card-front .brand-square { width: 34px; height: 34px; background: var(--lime); }
  .card-front .brand-name .line-main { font-size: 26px; }
  .card-front .brand-name .line-sub { font-size: 13px; letter-spacing: 6px; }
  .slogan {
    position: absolute; left: 36px; top: 100px;
    font-size: 13px; letter-spacing: 1px; color: var(--lime);
  }
  .decor-circle {
    position: absolute; right: -150px; top: -60px;
    width: 400px; height: 400px;
  }
  .contact {
    position: absolute; left: 36px; top: 148px;
    color: var(--text-grey); font-size: 12px; line-height: 1.5;
  }
  .person-name { font-size: 18px; font-weight: 700; color: var(--olive-dark); margin-bottom: 4px; }
  .contact-list { list-style: none; margin-top: 4px; }
  .contact-list li { display: flex; align-items: center; gap: 8px; }
  .contact-list svg { width: 12px; height: 12px; fill: var(--olive-dark); flex: none; }
</style>
</head>
<body>

<section class="card card-back">
  <div class="brand">
    <span class="brand-square"></span>
    <span class="brand-name"><span class="line-main">BREVEL</span><span class="line-sub">COATINGS</span></span>
  </div>
  <p class="website">www.brevel-coatings.com</p>
</section>

<section class="card card-front">
  <svg class="decor-circle" viewBox="0 0 400 400" aria-hidden="true">
    <defs>
      <linearGradient id="circleFill" x1="0" y1="0" x2="1" y2="1">
        <stop offset="0" stop-color="#c4dc4e"/>
        <stop offset="1" stop-color="#8fb52c"/>
      </linearGradient>
    </defs>
    <circle cx="200" cy="200" r="190" fill="url(#circleFill)"/>
  </svg>

  <div class="brand">
    <span class="brand-square"></span>
    <span class="brand-name"><span class="line-main">BREVEL</span><span class="line-sub">COATINGS</span></span>
  </div>
  <p class="slogan">making change simple</p>

  <div class="contact">
    <p class="person-name">Doran Vask</p>
    <p>2170 Harlow Lane</p>
    <p>Ridgefield, NY 10990</p>
    <ul class="contact-list">
      <li><svg viewBox="0 0 12 12"><path d="M1 4c0-2 2-3 5-3s5 1 5 3l-2 1-1-1H4L3 5zM3 6h6l1 5H2z"/></svg>(555) 416-9073</li>
      <li><svg viewBox="0 0 12 12"><rect x="3" y="0.5" width="6" height="11" rx="1"/><rect x="4" y="2" width="4" height="7" fill="#fff"/></svg>(555) 416-9074</li>
      <li><svg viewBox="0 0 12 12"><rect x="1" y="4" width="10" height="7"/><rect x="3" y="1" width="6" height="3"/></svg>(555) 416-9075</li>
      <li><svg viewBox="0 0 12 12"><rect x="0.5" y="2.5" width="11" height="7"/><path d="M0.5 2.5L6 7l5.5-4.5" stroke="#fff" fill="none"/></svg>d.vask@brevel-coatings.com</li>
    </ul>
  </div>
</section>

</body>
</html>
```